A wordpress website for the coolest Resort App

We have developed a mobile app - Zorbo and we want to develop a cool, neat and simple wordpress website for it.

I have attached the basics in a keynote/ ppt - but i need you to bring it more to life. plus there are additions:

FOr the number of pages, we will have:
1- Home: very similar to the one pager
2- How it works: Showing step by step on how the app works, and how it connects to the POS system of the restaurant etc with spanshots from the app
3- Benefit: Elaborating more on each of the benefits that is mentioned in the ONE PAGE document, with additional statistics, reference etc.. and embedded videos and animation
4- who we are page
5- In the press page: links to the articles where zorbo was mentioned
6- Get in touch page
7- FAQ
Updates

Target Market(s)

Resorts, hotels, beach and pool restaurant operators

Industry/Entity Type

Hospitality

Coding

Coded - Design and coding required

Font styles to use
Other font styles liked:
• I have attached the fonts i want to use: ROboto is the main font

Colors

Designer to choose colors to be used in the design.

Requirements
Must have
• Logo, icons for each benefit, you can also use the mood picture i attached or any other picture you recommend - maybe just something related to the app
• I also attached the Main colour, the orange and the blue is the accent one
• I attached the fonts, roboto is the main one
• there should also be a contact us:
• Email : info@zorboapp-mail.com
• Mobile: +971 5 23 47 90 18
• Address: Palm Quarter - Dubai - United Arab Emirates

```html
<!DOCTYPE html>
<html lang="en">
<head>
<meta charset="utf-8">
<title>Zorbo – Resort App</title>
<link href="https://fonts.googleapis.com/css2?family=Roboto:wght@400;500;700&family=Open+Sans:wght@400;600&display=swap" rel="stylesheet">
<style>
:root{
  --orange:#f26a3d;
  --blue:#2b93c9;
  --blue-dark:#1f7fb2;
  --dark:#2f323a;
  --ink:#222;
  --muted:#777;
  --line:#d9d9d9;
  --white:#fff;
}
*{box-sizing:border-box;margin:0;padding:0}
html,body{width:1200px;height:4891px;overflow:hidden}
body{font-family:"Open Sans",Arial,sans-serif;color:var(--ink);background:var(--white);position:relative}
h1,h2,h3,h4,.nav,.brand{font-family:"Roboto",Arial,sans-serif}
section,header,footer{position:absolute;left:0;width:1200px}

/* hero */
.hero{top:0;height:620px;overflow:hidden}
.hero-photo{position:absolute;inset:0;background:linear-gradient(180deg,#5e8fb0 0%,#8db6c9 30%,#7bb1bd 50%,#caa88a 70%,#b88f70 100%)}
.hero-shade{position:absolute;inset:0;background:rgba(20,30,40,.25)}
.brand{position:absolute;left:98px;top:32px;display:flex;align-items:center;gap:12px;color:var(--white);font-size:40px;font-weight:700;letter-spacing:.5px}
.brand-dot{width:22px;height:22px;border-radius:50%;background:var(--white)}
.nav{position:absolute;right:90px;top:50px;display:flex;gap:26px;font-size:14px;font-weight:700;color:var(--white);text-transform:uppercase}
.nav .active{color:var(--orange)}
.hero h1{position:absolute;top:240px;width:100%;text-align:center;color:var(--white);font-size:46px;font-weight:500;line-height:58px}
.dots{position:absolute;top:492px;width:100%;display:flex;justify-content:center;gap:8px}
.dots span{width:11px;height:11px;border-radius:50%;border:2px solid var(--white)}
.dots span:first-child{background:var(--white)}
.wave{position:absolute;left:0;bottom:0}

/* how it works */
.how{top:620px;height:668px}
.how h2{position:absolute;left:98px;top:68px;font-size:32px;font-weight:500}
.how .intro{position:absolute;left:98px;top:128px;width:560px;font-size:14px;line-height:24px;color:var(--muted)}
.steps{position:absolute;left:98px;top:205px;list-style:none}
.steps li{display:flex;align-items:center;gap:22px;height:75px;font-family:"Roboto",sans-serif;font-size:20px;position:relative}
.steps li::after{content:"";position:absolute;left:27px;top:62px;width:2px;height:26px;background:var(--line)}
.steps li:last-child::after{display:none}
.num{width:56px;height:56px;border-radius:50%;border:2px solid var(--line);display:flex;align-items:center;justify-content:center;font-size:24px;color:var(--blue)}
.steps li:first-child .num{background:var(--blue);border-color:var(--blue);color:var(--white)}
.phone{position:absolute;left:717px;top:80px;width:252px;height:490px;border:3px solid #cfcfcf;border-radius:40px;background:#f6f6f6}
.phone-speaker{position:absolute;left:96px;top:30px;width:60px;height:6px;border-radius:3px;background:#ccc}
.phone-screen{position:absolute;left:16px;top:68px;width:214px;height:350px;background:var(--orange);display:flex;align-items:center;justify-content:center;color:var(--white);font-family:"Roboto",sans-serif;font-size:40px;font-weight:700}
.phone-button{position:absolute;left:101px;top:432px;width:44px;height:44px;border-radius:50%;border:2px solid #ccc}

/* guest benefits */
.guests{top:1288px;height:544px;background:var(--dark);color:var(--white)}
.guests h2,.resort h2{position:absolute;top:90px;width:100%;text-align:center;font-size:32px;font-weight:500}
.guest-item{position:absolute;top:178px;width:230px;text-align:center}
.guest-icon{width:160px;height:160px;border-radius:50%;margin:0 auto 26px;display:flex;align-items:center;justify-content:center}
.guest-item h3{font-size:20px;font-weight:700;margin-bottom:14px}
.guest-item p{font-size:13px;line-height:20px;color:#d8d8d8}

/* resort benefits */
.resort{top:1832px;height:695px;background:var(--blue);color:var(--white)}
.resort svg{position:absolute;left:0;top:0}
.r-label{position:absolute;width:270px;font-family:"Roboto",sans-serif;font-size:16px;font-weight:500;line-height:22px}
.r-left{text-align:right}
.hub-name{position:absolute;left:543px;top:318px;width:120px;text-align:center;font-family:"Roboto",sans-serif;font-size:28px;font-weight:700;color:var(--white)}

/* who we are */
.who{top:2527px;height:505px}
.who h2,.press h2,.faq h2{position:absolute;top:92px;width:100%;text-align:center;font-size:32px;font-weight:500}
.who-item{position:absolute;text-align:center;font-family:"Roboto",sans-serif;font-size:20px;font-weight:500}
.who-circle{border-radius:50%;margin:0 auto 22px;border:8px solid var(--white);box-shadow:0 0 0 3px currentColor;display:flex;align-items:center;justify-content:center}
.divider{position:absolute;left:98px;top:500px;width:1004px;height:1px;background:var(--line)}

/* press */
.press{top:3032px;height:636px}
.press h2{top:70px}
.card{position:absolute;top:150px;width:316px}
.card-photo{height:195px}
.card h3{font-size:18px;font-weight:500;margin:40px 0 12px}
.meta{font-size:12px;color:var(--muted);margin-bottom:14px}
.card p{font-size:13px;line-height:20px;color:var(--muted)}
.more{display:block;margin-top:14px;font-family:"Roboto",sans-serif;font-size:13px;font-weight:700;color:var(--orange);text-transform:uppercase}

/* contact */
.contact{top:3668px;height:603px;color:var(--white);overflow:hidden}
.contact-photo{position:absolute;inset:0;background:linear-gradient(120deg,#3a3632 0%,#4a4038 45%,#6b5844 75%,#8a6e52 100%)}
.contact-shade{position:absolute;inset:0;background:rgba(20,20,24,.55)}
.contact h2{position:absolute;top:60px;width:100%;text-align:center;font-size:32px;font-weight:500}
.contact .sub{position:absolute;top:118px;width:100%;text-align:center;font-size:14px;line-height:24px}
.col-title{position:absolute;top:208px;font-family:"Roboto",sans-serif;font-size:14px;font-weight:700;text-transform:uppercase}
.field{position:absolute;height:34px;background:var(--white);border-radius:2px;color:#999;font-size:11px;padding:10px 12px;text-transform:uppercase}
.submit{position:absolute;left:630px;top:438px;width:100px;height:34px;border-radius:17px;background:var(--orange);color:var(--white);font-family:"Roboto",sans-serif;font-size:12px;font-weight:700;text-align:center;line-height:34px}
.info{position:absolute;left:808px;display:flex;gap:22px;align-items:flex-start;font-size:13px;line-height:20px}
.info-icon{width:36px;height:36px;border-radius:50%;border:1px solid rgba(255,255,255,.6);display:flex;align-items:center;justify-content:center;flex:none}

/* faq */
.faq{top:4271px;height:554px}
.faq h2{top:34px}
.faq-item{position:absolute;left:170px;width:864px;height:42px;border:1px solid var(--line);display:flex;align-items:center;font-family:"Roboto",sans-serif;font-size:17px;color:var(--blue-dark)}
.faq-toggle{width:42px;height:42px;flex:none;background:var(--blue);color:var(--white);font-size:24px;display:flex;align-items:center;justify-content:center;margin:-1px 18px -1px -1px}
.faq-item.open{background:var(--orange);border-color:var(--orange);color:var(--white)}
.faq-item.open .faq-toggle{background:#d9532a}
.faq-answer{position:absolute;left:170px;width:864px;padding:16px 20px;background:#f4f4f4;font-size:13px;line-height:22px;color:var(--muted)}

/* footer */
.site-footer{top:4825px;height:66px;background:#f1f1f1;display:flex;align-items:center;justify-content:space-between;padding:0 98px;font-size:12px;color:var(--muted)}
.social{display:flex;gap:14px}
.social span{width:22px;height:22px;background:#aaa;border-radius:3px}
</style>
</head>
<body>

<header class="hero">
  <div class="hero-photo" role="img" aria-label="Photo of a couple relaxing in striped deck chairs on a sunny beach"></div>
  <div class="hero-shade"></div>
  <div class="brand"><span class="brand-dot"></span>zorbo</div>
  <nav class="nav">
    <span class="active">Home</span><span>How it works</span><span>Benefit</span><span>Who we are</span><span>In the press</span><span>Get in touch</span><span>FAQ</span>
    <svg width="16" height="16" viewBox="0 0 16 16"><circle cx="6.5" cy="6.5" r="5" fill="none" stroke="#fff" stroke-width="2"/><line x1="10" y1="10" x2="15" y2="15" stroke="#fff" stroke-width="2"/></svg>
  </nav>
  <h1>Your smart solution to enhance your<br>business performance</h1>
  <div class="dots"><span></span><span></span><span></span><span></span></div>
  <svg class="wave" width="1200" height="120" viewBox="0 0 1200 120">
    <path d="M0 50 C300 120 700 0 1200 70 L1200 120 L0 120Z" fill="#fff"/>
    <path d="M0 50 C300 120 700 0 1200 70" fill="none" stroke="#f26a3d" stroke-width="5"/>
  </svg>
</header>

<section class="how">
  <h2>How It Works</h2>
  <p class="intro">Zorbo is a smart mobile app that the resort guests download it on their mobile. Through this app, the user locates himself and then can:</p>
  <ol class="steps">
    <li><span class="num">1</span>Check the menu</li>
    <li><span class="num">2</span>Order the food &amp; drinks</li>
    <li><span class="num">3</span>Call the waiter</li>
    <li><span class="num">4</span>Send requests to the waiter</li>
    <li><span class="num">5</span>Checkout and pay</li>
  </ol>
  <div class="phone">
    <div class="phone-speaker"></div>
    <div class="phone-screen">zorbo</div>
    <div class="phone-button"></div>
  </div>
</section>

<section class="guests">
  <h2>The Benefits For The Guests</h2>
  <div class="guest-item" style="left:68px">
    <div class="guest-icon" role="img" aria-label="Menu icon" style="background:#f6b91e">
      <svg width="80" height="80" viewBox="0 0 80 80"><rect x="20" y="10" width="40" height="60" rx="3" fill="#fff"/><g stroke="#f6b91e" stroke-width="4" stroke-linecap="round"><line x1="28" y1="24" x2="52" y2="24"/><line x1="28" y1="36" x2="52" y2="36"/><line x1="28" y1="46" x2="46" y2="46"/><line x1="28" y1="56" x2="50" y2="56"/></g></svg>
    </div>
    <h3>Menu</h3>
    <p>See a visual for each item, and have all relevant dietary details provided to them – including allergens</p>
  </div>
  <div class="guest-item" style="left:351px">
    <div class="guest-icon" role="img" aria-label="Stopwatch icon" style="background:#f26a3d">
      <svg width="80" height="80" viewBox="0 0 80 80"><rect x="34" y="6" width="12" height="8" rx="2" fill="#fff"/><circle cx="40" cy="44" r="26" fill="none" stroke="#fff" stroke-width="6"/><g stroke="#fff" stroke-width="5" stroke-linecap="round"><line x1="40" y1="44" x2="40" y2="28"/><line x1="40" y1="44" x2="51" y2="51"/></g></svg>
    </div>
    <h3>Speed</h3>
    <p>No more time lost catching a waiter. Submit your orders/requests and lay back.</p>
  </div>
  <div class="guest-item" style="left:618px">
    <div class="guest-icon" role="img" aria-label="Smartphone with tick icon" style="background:#25b3b0">
      <svg width="80" height="80" viewBox="0 0 80 80"><rect x="22" y="8" width="36" height="64" rx="6" fill="none" stroke="#fff" stroke-width="5"/><circle cx="40" cy="63" r="3" fill="#fff"/><polyline points="30,36 38,44 51,28" fill="none" stroke="#fff" stroke-width="5" stroke-linecap="round" stroke-linejoin="round"/></svg>
    </div>
    <h3>Customization</h3>
    <p>Customize the order and avoid human error</p>
  </div>
  <div class="guest-item" style="left:879px">
    <div class="guest-icon" role="img" aria-label="Payment card icon" style="background:#2a5a8a">
      <svg width="80" height="80" viewBox="0 0 80 80"><rect x="8" y="18" width="64" height="44" rx="5" fill="#f6b91e"/><rect x="8" y="28" width="64" height="8" fill="#2a5a8a"/><rect x="16" y="46" width="20" height="6" rx="1" fill="#fff"/></svg>
    </div>
    <h3>Fast Checkout</h3>
    <p>Avoid waiting for the bill, use the saved credit card, or pay cash</p>
  </div>
</section>

<section class="resort">
  <h2>The Benefits For The Resort</h2>
  <svg width="1200" height="695" viewBox="0 0 1200 695">
    <g stroke="#fff" stroke-width="2" fill="none">
      <line x1="411" y1="212" x2="520" y2="290"/>
      <line x1="411" y1="310" x2="505" y2="325"/>
      <line x1="411" y1="408" x2="505" y2="350"/>
      <line x1="411" y1="502" x2="520" y2="390"/>
      <line x1="802" y1="212" x2="686" y2="290"/>
      <line x1="802" y1="310" x2="700" y2="325"/>
      <line x1="802" y1="408" x2="700" y2="350"/>
      <line x1="802" y1="502" x2="686" y2="390"/>
      <circle cx="603" cy="336" r="98" stroke-width="12" stroke-dasharray="120 18"/>
    </g>
    <circle cx="603" cy="336" r="78" fill="#fff"/>
    <circle cx="603" cy="336" r="70" fill="#2b93c9"/>
    <g fill="#fff">
      <circle cx="411" cy="212" r="34"/><circle cx="411" cy="310" r="34"/><circle cx="411" cy="408" r="34"/><circle cx="411" cy="502" r="34"/>
      <circle cx="802" cy="212" r="34"/><circle cx="802" cy="310" r="34"/><circle cx="802" cy="408" r="34"/><circle cx="802" cy="502" r="34"/>
      <circle cx="610" cy="520" r="34"/>
    </g>
    <g role="img" aria-label="Benefit icons">
      <circle cx="411" cy="212" r="26" fill="#f26a3d"/><circle cx="411" cy="310" r="26" fill="#f6b91e"/><circle cx="411" cy="408" r="26" fill="#f26a3d"/><circle cx="411" cy="502" r="26" fill="#e8423b"/>
      <circle cx="802" cy="212" r="26" fill="#f6b91e"/><circle cx="802" cy="310" r="26" fill="#f6b91e"/><circle cx="802" cy="408" r="26" fill="#e8423b"/><circle cx="802" cy="502" r="26" fill="#f26a3d"/>
      <circle cx="610" cy="520" r="26" fill="#f6b91e"/>
      <g fill="#fff" stroke="#fff" stroke-linecap="round" stroke-linejoin="round">
        <polygon points="414,198 402,215 410,215 407,226 420,208 412,208" stroke-width="1"/>
        <polyline points="400,310 408,318 422,302" fill="none" stroke-width="4"/>
        <path d="M402 399 L420 417 M420 399 L402 417" fill="none" stroke-width="4"/>
        <rect x="400" y="504" width="5" height="10" stroke="none"/><rect x="408" y="498" width="5" height="16" stroke="none"/><rect x="416" y="491" width="5" height="23" stroke="none"/>
        <polygon points="802,198 806,207 815,208 808,214 810,223 802,218 794,223 796,214 789,208 798,207" stroke="none"/>
        <path d="M793 302 L801 310 L793 318 M803 302 L811 310 L803 318" fill="none" stroke-width="4"/>
        <path d="M802 419 C790 410 790 398 797 398 C800 398 802 401 802 403 C802 401 804 398 807 398 C814 398 814 410 802 419Z" stroke="none"/>
        <rect x="792" y="492" width="20" height="20" rx="3" fill="none" stroke-width="3"/><polyline points="797,502 801,506 808,497" fill="none" stroke-width="3"/>
        <circle cx="610" cy="520" r="13" fill="none" stroke-width="3"/><circle cx="610" cy="520" r="6" fill="none" stroke-width="3"/><circle cx="610" cy="520" r="2" stroke="none"/>
      </g>
    </g>
  </svg>
  <div class="hub-name">zorbo</div>
  <div class="r-label r-left" style="left:80px;top:190px">Increase your Guest<br>Service speed by 50%</div>
  <div class="r-label r-left" style="left:80px;top:288px">Optimize 70% of the<br>waiter's chore</div>
  <div class="r-label r-left" style="left:80px;top:386px">Avoid Human<br>Error</div>
  <div class="r-label r-left" style="left:80px;top:480px">Increase Your Average<br>Check Value</div>
  <div class="r-label" style="left:864px;top:190px">Sharpen Your<br>Offering</div>
  <div class="r-label" style="left:864px;top:299px">Go Fast &amp; Green</div>
  <div class="r-label" style="left:864px;top:397px">Build Loyalty</div>
  <div class="r-label" style="left:864px;top:480px">Achieve Higher<br>Completion Rate</div>
  <div class="r-label" style="left:475px;top:570px;text-align:center">Reach Your<br>Target Group</div>
</section>

<section class="who">
  <h2>Who we are</h2>
  <div class="who-item" style="left:113px;top:180px;color:#2a5a8a">
    <div class="who-circle" role="img" aria-label="Location pin icon" style="width:140px;height:140px;background:#2f4f63">
      <svg width="56" height="56" viewBox="0 0 56 56"><path d="M28 4C18 4 11 11 11 21c0 13 17 31 17 31s17-18 17-31C45 11 38 4 28 4z" fill="#e8423b"/><circle cx="28" cy="21" r="7" fill="#fff"/></svg>
    </div><span style="color:var(--ink)">Locate</span></div>
  <div class="who-item" style="left:321px;top:180px;color:#8b2b73">
    <div class="who-circle" role="img" aria-label="Open book icon" style="width:140px;height:140px;background:#8b2b73">
      <svg width="64" height="56" viewBox="0 0 64 56"><path d="M4 8 H28 Q32 8 32 12 V50 Q32 46 28 46 H4Z" fill="#f6d9a6"/><path d="M60 8 H36 Q32 8 32 12 V50 Q32 46 36 46 H60Z" fill="#fff"/><g stroke="#8b2b73" stroke-width="2"><line x1="10" y1="18" x2="26" y2="18"/><line x1="10" y1="26" x2="26" y2="26"/><line x1="10" y1="34" x2="22" y2="34"/><line x1="38" y1="18" x2="54" y2="18"/><line x1="38" y1="26" x2="54" y2="26"/><line x1="38" y1="34" x2="50" y2="34"/></g></svg>
    </div><span style="color:var(--ink)">Browse</span></div>
  <div class="who-item" style="left:497px;top:150px;color:#25b3b0">
    <div class="who-circle" role="img" aria-label="Plate with fork and knife icon" style="width:200px;height:200px;background:#2aa39b">
      <svg width="100" height="80" viewBox="0 0 100 80"><circle cx="50" cy="40" r="30" fill="#fff"/><circle cx="50" cy="40" r="20" fill="none" stroke="#2aa39b" stroke-width="3"/><g stroke="#fff" stroke-width="5" stroke-linecap="round"><line x1="8" y1="10" x2="8" y2="72"/><line x1="92" y1="10" x2="92" y2="72"/></g><g stroke="#fff" stroke-width="2"><line x1="3" y1="10" x2="3" y2="26"/><line x1="13" y1="10" x2="13" y2="26"/></g></svg>
    </div><span style="color:var(--ink)">Order</span></div>
  <div class="who-item" style="left:735px;top:180px;color:#2a6fb0">
    <div class="who-circle" role="img" aria-label="Lifebuoy icon" style="width:140px;height:140px;background:#2a6fb0">
      <svg width="64" height="64" viewBox="0 0 64 64"><circle cx="32" cy="32" r="22" fill="none" stroke="#fff" stroke-width="12"/><circle cx="32" cy="32" r="22" fill="none" stroke="#e8423b" stroke-width="12" stroke-dasharray="17.3 17.3" stroke-dashoffset="8.6"/></svg>
    </div><span style="color:var(--ink)">Help</span></div>
  <div class="who-item" style="left:941px;top:180px;color:#e54a7c">
    <div class="who-circle" role="img" aria-label="Banknote icon" style="width:140px;height:140px;background:#e54a7c">
      <svg width="70" height="50" viewBox="0 0 70 50"><rect x="10" y="4" width="56" height="32" rx="3" fill="#bfe3c3"/><rect x="4" y="14" width="56" height="32" rx="3" fill="#fff"/><circle cx="32" cy="30" r="9" fill="none" stroke="#e54a7c" stroke-width="3"/></svg>
    </div><span style="color:var(--ink)">Pay</span></div>
  <div class="divider"></div>
</section>

<section class="press">
  <h2>In the Press</h2>
  <article class="card" style="left:98px">
    <div class="card-photo" role="img" aria-label="Photo of hands using a smartphone at a desk" style="background:linear-gradient(135deg,#6b4a34,#a07c5c)"></div>
    <h3>Finibus Bonorum et Malorum</h3>
    <div class="meta">Mar 15, 2017 &nbsp;·&nbsp; admin</div>
    <p>At vero eos et accusamus et iusto odio dignissimos ducimus qui blanditiis praesentium voluptatum deleniti atque corrupti quos dolo.</p>
    <span class="more">Read more</span>
  </article>
  <article class="card" style="left:443px">
    <div class="card-photo" role="img" aria-label="Photo of berry smoothies on a wooden table" style="background:linear-gradient(135deg,#c3a6c8,#7f6b8f)"></div>
    <h3>Finibus Bonorum et Malorum</h3>
    <div class="meta">Mar 15, 2017 &nbsp;·&nbsp; admin</div>
    <p>At vero eos et accusamus et iusto odio dignissimos ducimus qui blanditiis praesentium voluptatum deleniti atque corrupti quos dolo.</p>
    <span class="more">Read more</span>
  </article>
  <article class="card" style="left:786px">
    <div class="card-photo" role="img" aria-label="Photo of red iced drinks with lime" style="background:linear-gradient(135deg,#d8363f,#8fbf6a)"></div>
    <h3>Finibus Bonorum et Malorum</h3>
    <div class="meta">Mar 15, 2017 &nbsp;·&nbsp; admin</div>
    <p>At vero eos et accusamus et iusto odio dignissimos ducimus qui blanditiis praesentium voluptatum deleniti atque corrupti quos dolo.</p>
    <span class="more">Read more</span>
  </article>
</section>

<section class="contact">
  <div class="contact-photo" role="img" aria-label="Photo of a cocktail beside a pool at sunset"></div>
  <div class="contact-shade"></div>
  <h2>Get in touch</h2>
  <p class="sub">Here there will be a contact us box where the user can write his message<br>and send it to our email, also we need to put these details</p>
  <div class="col-title" style="left:98px">Contact form</div>
  <div class="col-title" style="left:808px">Contact information</div>
  <div class="field" style="left:98px;top:250px;width:310px">Name</div>
  <div class="field" style="left:420px;top:250px;width:310px">Phone No.</div>
  <div class="field" style="left:98px;top:296px;width:632px">Email</div>
  <div class="field" style="left:98px;top:342px;width:632px;height:80px">Message</div>
  <div class="submit">SUBMIT</div>
  <div class="info" style="top:250px"><span class="info-icon"><svg width="14" height="18" viewBox="0 0 14 18"><path d="M7 0C3 0 0 3 0 7c0 5 7 11 7 11s7-6 7-11c0-4-3-7-7-7z" fill="#fff"/><circle cx="7" cy="7" r="2.5" fill="#3a3632"/></svg></span><span>Palm Quarter - Dubai<br>United Arab Emirates</span></div>
  <div class="info" style="top:318px"><span class="info-icon"><svg width="16" height="16" viewBox="0 0 16 16"><path d="M3 1l3 3-2 2c1 2 3 4 5 5l2-2 3 3-2 3C6 15 1 10 0 4z" fill="#fff"/></svg></span><span style="padding-top:8px">+971 5 23 47 90 18</span></div>
  <div class="info" style="top:378px"><span class="info-icon"><svg width="16" height="12" viewBox="0 0 16 12"><rect width="16" height="12" fill="#fff"/><path d="M0 0l8 7 8-7" fill="none" stroke="#3a3632" stroke-width="1.5"/></svg></span><span style="padding-top:8px">info@zorboapp-mail.com</span></div>
</section>

<section class="faq">
  <h2>FAQ</h2>
  <div class="faq-item open" style="top:104px"><span class="faq-toggle">−</span>At vero eos et accusamus et iusto odio dignissimos ducimus qui blanditiis voluptatum</div>
  <div class="faq-answer" style="top:146px">Nam libero tempore, cum soluta nobis est eligendi optio cumque nihil impedit quo minus id quod maxime placeat facere possimus, omnis voluptas assumenda est, omnis dolor repellendus autem quibusdam et aut.</div>
  <div class="faq-item" style="top:251px"><span class="faq-toggle">+</span>At vero eos et accusamus et iusto odio dignissimos ducimus qui blanditiis voluptatum</div>
  <div class="faq-item" style="top:309px"><span class="faq-toggle">+</span>At vero eos et accusamus et iusto odio dignissimos ducimus qui blanditiis voluptatum</div>
  <div class="faq-item" style="top:367px"><span class="faq-toggle">+</span>At vero eos et accusamus et iusto odio dignissimos ducimus qui blanditiis voluptatum</div>
  <div class="faq-item" style="top:426px"><span class="faq-toggle">+</span>At vero eos et accusamus et iusto odio dignissimos ducimus qui blanditiis voluptatum</div>
  <div class="faq-item" style="top:485px"><span class="faq-toggle">+</span>At vero eos et accusamus et iusto odio dignissimos ducimus qui blanditiis voluptatum</div>
</section>

<footer class="site-footer">
  <span>Copyrights © 2017, Zorbo All Rights Reserved. Privacy statement</span>
  <div class="social"><span></span><span></span><span></span><span></span></div>
</footer>

</body>
</html>
```